Poster for teenagers

Bright, trendy, modern and young fonts - a variety of fonts, plus arrows and clip art (no photos) for an A3 size poster to be hung in study halls of schools. There are six dot points. I think each point should be in some kind of box or circle.

Here are a few ideas of the kind of thing I mean.
http://www.tarnwick.example.au/Page/Images/youth_Advisory_Group_Poster_(1).jpg

http://www.holmbrae.example.ie/sites/default/files/Youth-Panel-Poster-1-Web.jpg

http://www.quillmarsh.example.au/images/librariesprovider4/Misc-illustrations/140335-qml-youth-superheros-heroup-highres.jpg?sfvrsn=0

https://rvkointernational.files.examplepress.com/2013/04/544477_432153653542694_970534114_n.jpg

Also my logo should be on it some where . I've attached a my logo.

Here is the text:
How to get organised and motivated this year.
1. Write stuff down
Write down things you need to do and when you plan to do them. Use digital calendars, to do apps and email lists – or pen and paper. Even if you are sure you will remember – get it out of your head and onto paper/your phone/laptop. You are more likely to get it done and feel less stressed.
2. Set up habits
If you do things in the same way, at the same time or after the same thing – then after a few weeks, it becomes much easier to get those things done. Set up a particular time, or place to do study tasks – or link them with another daily task. EG: art homework every Tuesday. Violin practice after breakfast.
3. Focus!
For 15-30 minutes at a time - totally focus on homework. Put your phone away, log out of chatterbox, close down other programs and really concentrate. Then have a break, send a text or whatever – and then go back to focussed study. Fifteen minutes of concentrated study gets more achieved than an hour of study switching back and forth between homework and other activities.
4. Just do something
No motivation? Just take a “bite”. Set a timer and just do 5 minutes. Or 15. Or read just the first two pages. Or the first problem on the worksheet. Something is better than nothing – and sometimes once you start, it’s easier to keep going.
5. Use rewards and consequences
Reward yourself when you do a hard task and use consequences when you don’t. Use food, fun activities, gaming and social time to motivate yourself – you get it when you do tasks, you don’t when you don’t. EG 15 minutes of vidloop when I finish this page. Tell other people your plans and you are more likely to stick to them.
6. Imagine the future
When you really can’t be find any motivation to do the things you need to do – take 30 seconds to think about what will happen in a week, month and year if you get on with it. What will happen then and how will that feel. And imagine what will happen in a week, month and year if you DON’T do those things – and how will that feel.

Good luck !
For free articles and one to one help with study skills, increasing motivation, coping with stress or tough times in senior school, go to brightpathlearning.example.au
Brightpath Learning Psychology and Education

```html
<!DOCTYPE html>
<html lang="en">
<head>
<meta charset="utf-8">
<title>How to Get Organised and Motivated This Year</title>
<link rel="stylesheet" href="https://fonts.googleapis.com/css2?family=Bebas+Neue&family=Lobster&family=Oswald:wght@400&display=swap">
<style>
  :root {
    --ink: #111111;
    --paper: #ffffff;
    --shadow: #d6d6d6;
    --green: #3d9a2c;
    --red: #d81b2b;
    --purple: #7b2e9f;
    --amber: #f8a31c;
    --navy: #1e2479;
    --flame: #f04a1f;
    --brand: #4e7d2a;
  }
  * { box-sizing: border-box; margin: 0; padding: 0; }
  html, body { width: 849px; height: 1200px; overflow: hidden; background: var(--paper); }
  .poster { position: relative; width: 849px; height: 1200px; background: var(--paper); overflow: hidden; }
  .frame {
    position: absolute; left: 29px; top: 31px; width: 792px; height: 1140px;
    border: 4px solid var(--ink);
  }
  .shadows { position: absolute; inset: 0; }
  .brand {
    position: absolute; left: 640px; top: 44px;
    display: flex; align-items: center; gap: 8px;
    font-family: "Oswald", sans-serif; font-weight: 400;
    color: var(--brand); font-size: 15px; line-height: 1.05; text-transform: uppercase;
  }
  .brand-dot { width: 34px; height: 34px; border-radius: 50%; background: var(--brand); flex: none; }
  .headline {
    position: absolute; left: 74px; top: 78px;
    font-family: "Bebas Neue", sans-serif; color: var(--ink); text-transform: uppercase;
  }
  .headline .lead { display: block; font-size: 36px; line-height: 1; margin-bottom: 24px; }
  .headline .main { display: block; font-size: 82px; line-height: 0.82; }
  .headline .small { font-size: 50px; }

  .tip { position: absolute; color: var(--paper); }
  .tip h2 {
    font-family: "Lobster", cursive; font-weight: 400;
    font-size: 36px; line-height: 1; text-align: center;
  }
  .tip p {
    font-family: "Oswald", sans-serif; font-size: 12.6px; line-height: 18px;
    text-transform: uppercase;
  }
  .tip .icon { float: left; width: 56px; height: 60px; margin: 0 12px 4px 0; }
  .tip .icon svg { width: 100%; height: 100%; fill: none; stroke: var(--paper); stroke-width: 2.5; stroke-linecap: round; stroke-linejoin: round; }

  .tip-write { left: 0; top: 309px; width: 423px; height: 256px; background: var(--green); padding: 14px 22px 0 40px; }
  .tip-write .icon { margin-left: 58px; }
  .tip-write p { margin-top: 16px; }

  .tip-habits { left: 423px; top: 309px; width: 349px; height: 256px; background: var(--red); padding: 14px 14px 0 20px; }
  .tip-habits p { margin-top: 16px; }

  .tip-focus { left: 73px; top: 565px; width: 350px; height: 258px; background: var(--purple); padding: 14px 16px 0 20px; }
  .tip-focus p { margin-top: 18px; }

  .tip-start { left: 423px; top: 565px; width: 426px; height: 258px; background: var(--amber); padding: 14px 40px 0 20px; }
  .tip-start p { margin-top: 18px; }

  .tip-reward { left: 0; top: 823px; width: 423px; height: 260px; background: var(--navy); padding: 8px 16px 0 92px; }
  .tip-reward h2 { margin-left: -92px; line-height: 0.95; }
  .tip-reward p { margin-top: 10px; }

  .tip-future { left: 423px; top: 823px; width: 349px; height: 377px; background: var(--flame); padding: 14px 16px 0 22px; }
  .tip-future p { margin-top: 34px; }

  .signoff {
    position: absolute; left: 50px; top: 1086px; width: 370px;
    font-family: "Oswald", sans-serif; font-size: 9px; line-height: 14px;
    color: var(--ink); text-transform: uppercase;
  }
</style>
</head>
<body>
<main class="poster">
  <svg class="shadows" width="849" height="1200" aria-hidden="true">
    <polygon points="772,330 849,407 849,565 772,565" fill="var(--shadow)"/>
    <polygon points="0,565 73,565 73,640" fill="var(--shadow)"/>
    <polygon points="772,823 849,900 849,1200 772,1200" fill="var(--shadow)"/>
  </svg>
  <div class="frame"></div>

  <div class="brand"><span class="brand-dot"></span><span>Brightpath<br>Learning</span></div>

  <h1 class="headline">
    <span class="lead">How to</span>
    <span class="main">Get Organised <span class="small">and</span> Motivated<br>This Year</span>
  </h1>

  <section class="tip tip-write">
    <h2>Write stuff down</h2>
    <p><span class="icon"><svg viewBox="0 0 56 60"><path d="M12 6h30v40"/><path d="M12 6v44a6 6 0 0 1-6 6h32a6 6 0 0 0 6-6"/><path d="M18 16h18M18 23h18M18 30h18M18 37h14"/><path d="M6 56a6 6 0 0 1-2-10h8"/></svg></span>Write down things you need to do and when you plan to do them. Use digital calendars, to do apps and email lists – or pen and paper. Even if you are sure you will remember – get it out of your head and onto paper/your phone/laptop. You are more likely to get it done and feel less stressed.</p>
  </section>

  <section class="tip tip-habits">
    <h2>Set up habits</h2>
    <p><span class="icon"><svg viewBox="0 0 56 60"><path d="M10 26a18 18 0 0 1 32-8"/><path d="M44 10v9h-9"/><path d="M46 34a18 18 0 0 1-32 8"/><path d="M12 50v-9h9"/></svg></span>If you do things in the same way, at the same time or after the same thing – then after a few weeks, it becomes much easier to get those things done. Set up a particular time, or place to do study tasks – or link them with another daily task. EG: art homework every Tuesday. Violin practice after breakfast.</p>
  </section>

  <section class="tip tip-focus">
    <h2>Focus!</h2>
    <p><span class="icon"><svg viewBox="0 0 56 60"><circle cx="26" cy="32" r="22"/><circle cx="26" cy="32" r="14"/><circle cx="26" cy="32" r="5"/><path d="M26 32 50 8"/><path d="M44 8h6v6"/></svg></span>For 15-30 minutes at a time - totally focus on homework. Put your phone away, log out of chatterbox, close down other programs and really concentrate. Then have a break, send a text or whatever – and then go back to focussed study. Fifteen minutes of concentrated study gets more achieved than an hour of study switching back and forth between homework and other activities.</p>
  </section>

  <section class="tip tip-start">
    <h2>Just do something</h2>
    <p><span class="icon"><svg viewBox="0 0 56 60"><path d="M10 26h30v28H10z"/><path d="M40 32h6a5 5 0 0 1 0 10h-6"/><path d="M16 26V8l4-4 4 4v18"/><path d="M28 26V12h8v14"/></svg></span>No motivation? Just take a “bite”. Set a timer and just do 5 minutes. Or 15. Or read just the first two pages. Or the first problem on the worksheet. Something is better than nothing – and sometimes once you start, it’s easier to keep going.</p>
  </section>

  <section class="tip tip-reward">
    <h2>Use rewards<br>and consequences</h2>
    <p><span class="icon"><svg viewBox="0 0 56 60"><circle cx="28" cy="30" r="24"/><path d="M17 31l8 8 15-17"/></svg></span>Reward yourself when you do a hard task and use consequences when you don’t. Use food, fun activities, gaming and social time to motivate yourself – you get it when you do tasks, you don’t when you don’t. EG 15 minutes of vidloop when I finish this page. Tell other people your plans and you are more likely to stick to them.</p>
  </section>

  <section class="tip tip-future">
    <h2>Imagine the future</h2>
    <p><span class="icon"><svg viewBox="0 0 56 60"><rect x="6" y="8" width="44" height="44" rx="8"/><circle cx="28" cy="30" r="15"/><path d="M28 20v10h8"/></svg></span>When you really can’t be find any motivation to do the things you need to do – take 30 seconds to think about what will happen in a week, month and year if you get on with it. What will happen then and how will that feel. And imagine what will happen in a week, month and year if you don’t do those things – and how will that feel.</p>
  </section>

  <footer class="signoff">
    Good luck !<br>
    For free articles and one to one help with study skills, increasing motivation, coping with stress or tough times in senior school, go to brightpathlearning.example.au<br>
    Brightpath Learning Psychology and Education
  </footer>
</main>
</body>
</html>
```